依頼詳細
デザイン指示書を参考に居抜き物件をリフォームして開業を考えている人向けにデザインをしていただきたいと思います。
お客様の理想の店舗デザインを実現します。全体のイメージは、スタイリッシュでオシャレで、高級感のあるデザインを希望します。
サイトURL
ページ数
1ページ
希望イメージ
シンプル 複雑
単色 カラフル
暗い 明るい
日常 高級
遊び心 厳粛
未来的 伝統的
女性的 男性的
希望する色
茶系
納品ファイル
• 高解像度JPG (.jpg)
• イラストレーター形式 (.ai)
• フォトショップ形式 (.psd)
補足説明
レスポンシブデザインでお願い致します。指示書の中の事例画像は、現在準備中のため、ご提案をお願いします。
依頼金額を40000円に変更して、延長しました。
■ 選んだ理由

シンプルなデザインありがとうございました。

修正を引き続きよろしくお願いいたします。

■ 提案者全員のお礼・コメント

たくさんのデザインありがとうございました。
今後もデザインコンペを行ってまいりますのでよろしくお願い致します。

```html
<!DOCTYPE html>
<html lang="ja">
<head>
<meta charset="utf-8">
<title>店舗リフォームのアオバ</title>
<link href="https://fonts.googleapis.com/css2?family=Noto+Serif+JP:wght@400;600;700&family=Noto+Sans+JP:wght@400;500&display=swap" rel="stylesheet">
<style>
:root{
  --ink:#121212;
  --panel:#242424;
  --panel-dark:#181818;
  --gold:#c8a96a;
  --gold-light:#d8bf8a;
  --text:#e6e1d6;
  --muted:#9a958c;
  --red:#b8141a;
  --red-deep:#5a0b0d;
  --line:#3a3a3a;
}
*{margin:0;padding:0;box-sizing:border-box}
html,body{width:1200px;height:2456px;overflow:hidden;background:var(--ink);color:var(--text);font-family:"Noto Sans JP",sans-serif}
.serif{font-family:"Noto Serif JP",serif}
.site-header{height:108px;background:var(--ink);display:flex;align-items:center;justify-content:space-between;padding:0 180px}
.brand{display:flex;align-items:center;gap:12px;font-family:"Noto Serif JP",serif;font-size:26px;color:var(--gold);letter-spacing:2px}
.brand-mark{width:14px;height:14px;background:var(--gold)}
.contact{display:flex;align-items:center;gap:14px;color:var(--text)}
.contact small{font-size:12px;color:var(--muted)}
.contact strong{font-family:"Noto Serif JP",serif;font-size:32px;font-weight:600;letter-spacing:1px}
.global-nav{height:40px;background:#0c0c0c;border-top:1px solid var(--line);display:flex;justify-content:center;gap:60px;align-items:center;font-size:14px}
.global-nav a{color:var(--text);text-decoration:none}
.hero{position:relative;height:410px;background:linear-gradient(135deg,var(--red-deep) 0%,var(--red) 40%,#e0452a 60%,var(--red) 80%,var(--red-deep) 100%)}
.hero h1{position:absolute;top:66px;left:0;right:0;text-align:center;font-family:"Noto Serif JP",serif;font-weight:600;font-size:44px;letter-spacing:6px;color:#fff;text-shadow:0 2px 8px rgba(0,0,0,.6)}
.features{background:var(--panel);padding:70px 180px 60px;height:702px}
.feature{margin-bottom:56px}
.feature h2{font-family:"Noto Serif JP",serif;font-weight:600;font-size:30px;color:var(--text);margin-bottom:14px}
.feature h2 span{font-size:14px;font-weight:400;margin-right:4px}
.feature p{font-size:14px;line-height:1.9;color:var(--muted)}
.dark{background:var(--ink);padding:50px 180px 0}
.section-title{font-family:"Noto Serif JP",serif;font-size:32px;font-weight:600;color:var(--text);margin-bottom:14px}
.section-title span{font-size:14px;font-weight:400}
.works{display:flex;gap:12px;margin-bottom:70px}
.works div{flex:1;height:112px;background:linear-gradient(160deg,var(--red-deep),var(--red) 50%,#d84a2c 70%,var(--red-deep))}
.columns{display:flex;gap:60px;margin-bottom:60px}
.column{flex:1}
.column h3{font-family:"Noto Serif JP",serif;font-size:24px;font-weight:600;padding-bottom:12px;border-bottom:1px solid var(--line);margin-bottom:16px}
.column li{list-style:none;display:flex;gap:28px;font-size:13px;line-height:2.4}
.column time{color:var(--text)}
.column .tag{color:var(--gold);width:96px}
.column .ttl{color:var(--gold-light)}
.buttons{display:flex;gap:60px;margin-bottom:70px}
.buttons a{flex:1;height:58px;background:var(--gold);color:var(--ink);display:flex;align-items:center;justify-content:center;font-size:22px;font-family:"Noto Serif JP",serif;font-weight:600;text-decoration:none;letter-spacing:2px}
.access{text-align:center;padding-bottom:24px}
.access h2{font-family:"Noto Serif JP",serif;font-size:26px;font-weight:600;margin-bottom:24px}
.access p{font-size:14px;display:flex;justify-content:center;align-items:center;gap:24px}
.map{height:392px;background:linear-gradient(120deg,#cfcfcf,#e2e2e2 50%,#c8c8c8)}
.site-footer{height:118px;background:var(--ink);text-align:center;padding-top:28px}
.site-footer nav{display:flex;justify-content:center;gap:44px;font-size:13px;margin-bottom:22px}
.site-footer nav a{color:var(--text);text-decoration:none}
.site-footer small{font-size:11px;color:var(--muted)}
</style>
</head>
<body>
<header class="site-header">
  <div class="brand"><span class="brand-mark"></span>店舗リフォームのアオバ</div>
  <div class="contact"><small>お問い合わせ</small><svg width="22" height="22" viewBox="0 0 24 24"><path fill="#e6e1d6" d="M6.6 10.8a15 15 0 0 0 6.6 6.6l2.2-2.2c.3-.3.7-.4 1-.2 1.1.4 2.3.6 3.6.6.6 0 1 .4 1 1V20c0 .6-.4 1-1 1A17 17 0 0 1 3 4c0-.6.4-1 1-1h3.5c.6 0 1 .4 1 1 0 1.3.2 2.5.6 3.6.1.3 0 .7-.2 1z"/></svg><strong>028-555-0187</strong></div>
</header>
<nav class="global-nav">
  <a href="#">HOME</a><a href="#">リフォームとは</a><a href="#">リフォーム工程</a><a href="#">施工事例</a><a href="#">会社概要</a><a href="#">お問い合わせ</a>
</nav>
<section class="hero" role="img" aria-label="赤い照明の和風個室店舗の内装写真">
  <h1>リフォームで理想の店舗に</h1>
</section>
<section class="features">
  <div class="feature">
    <h2><span>店舗リフォームの</span>こだわり</h2>
    <p>ここには店舗リフォームのこだわりについての説明文が入ります。素材選びから照明計画まで、お客様の理想に合わせた空間づくりを丁寧にご提案いたします。<br>居抜き物件の良さを活かしながら、高級感のある店舗へと仕上げます。</p>
  </div>
  <div class="feature">
    <h2><span>店舗リフォームの</span>注意点</h2>
    <p>ここには店舗リフォームの注意点についての説明文が入ります。設備の状態や法令の確認など、開業前に押さえておきたいポイントをわかりやすくご案内いたします。<br>事前の調査で予算と工期の見通しを立てます。</p>
  </div>
  <div class="feature">
    <h2><span>店舗リフォームの</span>アフターメンテナンス</h2>
    <p>ここには店舗リフォームのアフターメンテナンスについての説明文が入ります。開業後も定期点検や修繕のご相談に迅速に対応し、長く安心してお使いいただけます。<br>小さな不具合もお気軽にご連絡ください。</p>
  </div>
</section>
<section class="dark">
  <h2 class="section-title"><span>店舗リフォームの</span>施工事例</h2>
  <div class="works">
    <div role="img" aria-label="施工事例の店舗写真1"></div>
    <div role="img" aria-label="施工事例の店舗写真2"></div>
    <div role="img" aria-label="施工事例の店舗写真3"></div>
    <div role="img" aria-label="施工事例の店舗写真4"></div>
    <div role="img" aria-label="施工事例の店舗写真5"></div>
  </div>
  <div class="columns">
    <div class="column">
      <h3>新着情報</h3>
      <ul>
        <li><time>2016.06.20</time><span class="tag">店舗リフォーム</span><span class="ttl">施工事例を追加</span></li>
        <li><time>2016.06.14</time><span class="tag">お知らせ</span><span class="ttl">夏季休業のご案内</span></li>
        <li><time>2016.06.01</time><span class="tag">イベント</span><span class="ttl">相談会のお知らせ</span></li>
        <li><time>2016.05.18</time><span class="tag">お知らせ</span><span class="ttl">サイトをリニューアル</span></li>
      </ul>
    </div>
    <div class="column">
      <h3>リフォームコラム</h3>
      <ul>
        <li><time>2016.06.18</time><span class="ttl">リフォーム費用の目安</span></li>
        <li><time>2016.06.10</time><span class="ttl">居抜き物件の選び方</span></li>
        <li><time>2016.06.03</time><span class="ttl">照明で変わる店舗印象</span></li>
        <li><time>2016.05.25</time><span class="ttl">開業までの流れ</span></li>
      </ul>
    </div>
  </div>
  <div class="buttons"><a href="#">取扱メーカー</a><a href="#">店舗改修</a></div>
  <div class="access">
    <h2>アクセス</h2>
    <p><span><svg width="14" height="18" viewBox="0 0 14 18"><path fill="#c8a96a" d="M7 0a7 7 0 0 0-7 7c0 5 7 11 7 11s7-6 7-11a7 7 0 0 0-7-7zm0 9.5A2.5 2.5 0 1 1 7 4.5a2.5 2.5 0 0 1 0 5z"/></svg> 店舗リフォームのアオバ（株式会社アオバ）</span><span>〒320-0000 架空県中央市緑町1-2-3</span><span>TEL 028-555-0187</span></p>
  </div>
</section>
<div class="map" role="img" aria-label="店舗所在地周辺の地図"></div>
<footer class="site-footer">
  <nav><a href="#">リフォームとは</a><a href="#">リフォーム工程</a><a href="#">施工事例</a><a href="#">会社概要</a><a href="#">お問い合わせ</a></nav>
  <small>© 2016 店舗リフォームのアオバ</small>
</footer>
</body>
</html>
```